LQV Web Site

Build a web site for Distant Charting and Rostering (LQV)

Target Market(s)

Petrochemical, Refining, and Manufacturing

Industry/Entity Type

Manufacturing

Coding

Coded - Design and coding required

Number of Pages Required

1 page

Font styles to use
Sans Serif

Colors

Designer to choose only greyscale colors for use in the design.

Requirements
Must have
• LQV is a member of WEN Venture Services family of companies, along with Brivonta, and Mulvarde.
Would like LQV to mimic Brivonta, and Mulvarde in layout and functionality.
WIll use the same office address and phone # found Brivonta and Mulvarde.
The color scheme needs to match the logo colors.
The final product needs to be in word press.
would like to connect the QR code found on one-pager to the website.

Reference these websites: www.brivonta-example.com and www.mulvarde-example.com
Nice to have
• Would like to have a contact tab similar to the one found on Mulvarde website. Use this email address. (LQV@WEN.example.com)
The home page needs to have simple depictions of the problem statement, solution, and introduction to LQV. (use the video script to help, feel free to use your own words)

```html
<!DOCTYPE html>
<html lang="en">
<head>
<meta charset="utf-8">
<title>LQV – Distant Charting and Rostering</title>
<link rel="stylesheet" href="https://fonts.googleapis.com/css2?family=Khand:wght@500;600&family=Poppins:wght@400;500;600&display=swap">
<style>
:root{
  --bg:#f2f2f2;
  --white:#ffffff;
  --ink:#1c1c1c;
  --text:#3a3a3a;
  --muted:#6d6d6d;
  --line:#d9d9d9;
  --dark:#141518;
  --dark-2:#2b2d31;
  --logo:#7a7d83;
}
*{box-sizing:border-box;margin:0;padding:0}
html,body{width:1200px;height:2938px;overflow:hidden;background:var(--bg)}
body{font-family:'Poppins',sans-serif;color:var(--text)}
.page{position:absolute;left:106px;top:42px;width:987px;height:2853px;background:var(--white);box-shadow:0 4px 24px rgba(0,0,0,.08);overflow:hidden}
.heading{font-family:'Khand',sans-serif;font-weight:600;color:var(--ink);line-height:1}
.btn{display:inline-block;border:1.5px solid currentColor;border-radius:14px;font-size:9px;font-weight:500;padding:6px 24px;letter-spacing:.3px;text-transform:uppercase}
section,header,footer{position:relative}

/* header */
.site-header{height:93px;border-bottom:1px solid var(--line)}
.site-header .active-mark{position:absolute;top:0;left:299px;width:46px;height:3px;background:#777}
.brand{position:absolute;left:109px;top:28px;display:flex;align-items:center;gap:6px}
.brand .dot{width:10px;height:10px;border-radius:50%;background:var(--logo)}
.brand .name{font-family:'Khand',sans-serif;font-weight:600;font-size:34px;color:var(--logo);line-height:1}
.nav{position:absolute;top:40px;left:0;width:100%;font-family:'Khand',sans-serif;font-weight:500;font-size:14px;color:#555}
.nav a{position:absolute;color:inherit;text-decoration:none;white-space:nowrap}
.nav .search{position:absolute;left:880px;top:-1px}

/* hero */
.hero{height:435px;background:linear-gradient(100deg,#2a2c30 0%,#3b3e43 45%,#202226 75%,#2c2e33 100%);color:var(--white)}
.hero .media{position:absolute;right:0;top:0;width:55%;height:100%;background:radial-gradient(ellipse at 60% 45%,#4a4d53 0%,#25272b 70%)}
.hero .copy{position:absolute;left:109px;top:90px}
.hero h1{font-family:'Khand',sans-serif;font-weight:500;font-size:50px;line-height:.98;color:var(--white)}
.hero ul{list-style:none;margin-top:16px;font-size:13px;line-height:20.5px}
.hero li::before{content:"";display:inline-block;width:7px;height:7px;border-radius:50%;background:var(--white);margin-right:12px;vertical-align:1px}
.hero .btn{margin-top:20px;color:var(--white)}
.dots{position:absolute;left:0;right:0;bottom:14px;display:flex;justify-content:center;gap:8px;align-items:center}
.dots span{width:6px;height:6px;border-radius:50%;background:#ddd}
.dots span.on{width:8px;height:8px;background:#fff}

/* problem */
.problem{height:407px;text-align:center}
.problem h2{font-size:36px;padding-top:48px}
.problem-list{position:absolute;top:125px;left:0;width:100%}
.problem-item{position:absolute;width:186px;margin-left:-93px;text-align:center}
.problem-item svg{display:block;margin:0 auto}
.problem-item p{font-size:13px;line-height:16px;color:var(--ink);margin:26px auto 0;width:140px}

/* dark bands */
.band{color:var(--white)}
.band .heading{color:var(--white)}
.solution{height:290px;background:linear-gradient(90deg,#141517 0%,#232529 40%,#3a3d42 75%,#2a2c30 100%)}
.solution .copy{position:absolute;left:112px;top:68px;width:440px}
.solution h2{font-size:32px}
.solution p{font-size:12.5px;line-height:19.5px;margin-top:10px}
.solution .btn{margin-top:10px}

/* intro */
.intro{height:338px}
.intro .mark{position:absolute;left:118px;top:92px;display:flex;align-items:center;gap:14px}
.intro .mark .dot{width:26px;height:26px;border-radius:50%;background:#3c3f44}
.intro .mark .name{font-family:'Khand',sans-serif;font-weight:600;font-size:140px;line-height:1;color:#3c3f44}
.intro .copy{position:absolute;left:565px;top:108px;width:335px}
.intro h2{font-size:34px}
.intro p{font-size:14.5px;line-height:23.5px;margin-top:10px}

/* how it works */
.how{height:425px;background:linear-gradient(180deg,#07080c 0%,#111318 45%,#1f2024 75%,#121317 100%);text-align:center}
.how h2{font-size:32px;padding-top:44px}
.how-col{position:absolute;top:137px;width:238px;margin-left:-119px}
.how-col h3{font-family:'Khand',sans-serif;font-weight:600;font-size:24px;line-height:1;display:inline-block;padding-bottom:6px;border-bottom:2px solid var(--white)}
.how-col p{font-size:12.5px;line-height:18px;margin-top:14px}
.how-col .btn{margin-top:14px}

/* value */
.value{height:341px;text-align:center}
.value .eyebrow{font-family:'Khand',sans-serif;font-weight:500;font-size:16px;color:#444;padding-top:54px}
.value h2{font-size:32px;margin-top:2px}
.value p{width:612px;margin:16px auto 0;font-size:12.5px;line-height:20.5px;color:#555}
.value .btn{margin-top:24px;color:#444}

/* contact */
.contact{height:249px;background:linear-gradient(90deg,#15171b 0%,#25282d 50%,#181a1e 100%);text-align:center}
.contact h2{font-size:32px;padding-top:58px}
.contact p{font-size:12.5px;line-height:20px;width:630px;margin:20px auto 0}
.contact .btn{margin-top:12px}

/* footer */
.site-footer{height:242px}
.footer-brand{position:absolute;left:120px;top:50px;width:245px}
.footer-brand .brand-row{display:flex;align-items:center;gap:6px}
.footer-brand .dot{width:10px;height:10px;border-radius:50%;background:var(--logo)}
.footer-brand .name{font-family:'Khand',sans-serif;font-weight:600;font-size:36px;line-height:1;color:var(--logo)}
.footer-brand p{font-size:9px;line-height:13px;color:#333;margin-top:14px}
.footer-col{position:absolute;top:60px}
.footer-col h4{font-size:14px;font-weight:600;color:var(--ink);letter-spacing:.2px;white-space:nowrap}
.footer-col ul{list-style:none;margin-top:14px;font-size:9.5px;line-height:17.5px;color:#555}
.footer-col li{display:flex;gap:8px;align-items:flex-start;white-space:nowrap}
.footer-col li span{line-height:12px;margin-bottom:5px}
.footer-col svg{flex:none;margin-top:2px}
.social{display:flex;gap:16px;margin-top:16px}
.social span{width:13px;height:13px;border-radius:50%;background:var(--ink)}
.copyright{height:33px;background:#0d0d0d;color:#ccc;font-size:8px;display:flex;align-items:center;justify-content:center}
</style>
</head>
<body>
<main class="page">

  <header class="site-header">
    <span class="active-mark"></span>
    <div class="brand"><span class="dot"></span><span class="name">LQV</span></div>
    <nav class="nav">
      <a style="left:307px">HOME</a>
      <a style="left:374px">PROBLEM</a>
      <a style="left:460px">SOLUTION</a>
      <a style="left:551px">OUR PRODUCT</a>
      <a style="left:661px">HOW IT WORKS</a>
      <a style="left:775px">CONTACT</a>
      <svg class="search" width="16" height="16" viewBox="0 0 16 16"><circle cx="7" cy="7" r="5" fill="none" stroke="#555" stroke-width="1.4"/><line x1="10.6" y1="10.6" x2="14" y2="14" stroke="#555" stroke-width="1.4"/></svg>
    </nav>
  </header>

  <section class="hero">
    <div class="media" role="img" aria-label="Dark photograph of a profile silhouette overlaid with a glowing digital network"></div>
    <div class="copy">
      <h1>DISTANT CHARTING &amp;<br>ROSTERING</h1>
      <ul>
        <li>Fixed Price. Zero Cost Escalation</li>
        <li>Reduce Cost</li>
        <li>Reduce personnel on site</li>
        <li>Productivity Gains</li>
        <li>Easy to Monitor Progress</li>
      </ul>
      <span class="btn">Explore</span>
    </div>
    <div class="dots"><span></span><span class="on"></span><span></span></div>
  </section>

  <section class="problem">
    <h2 class="heading">The Problem</h2>
    <div class="problem-list">
      <div class="problem-item" style="left:229px">
        <svg width="148" height="148" viewBox="0 0 148 148"><defs><linearGradient id="ring" x1="0" y1="0" x2="1" y2="1"><stop offset="0" stop-color="#000"/><stop offset="1" stop-color="#3a3a3a"/></linearGradient></defs>
          <circle cx="74" cy="74" r="66" fill="none" stroke="url(#ring)" stroke-width="14"/>
          <g fill="none" stroke="#222" stroke-width="1.6"><rect x="54" y="56" width="40" height="36" rx="2"/><line x1="54" y1="65" x2="94" y2="65"/><line x1="62" y1="51" x2="62" y2="59"/><line x1="86" y1="51" x2="86" y2="59"/><path d="M60 71h28M60 78h28M60 85h20M67 66v24M74 66v24M81 66v24"/><circle cx="91" cy="90" r="6" fill="#fff"/><path d="M88 90l2 2 4-4"/></g></svg>
        <p>High cost for turnaround planning and scheduling</p>
      </div>
      <div class="problem-item" style="left:416px">
        <svg width="148" height="148" viewBox="0 0 148 148"><circle cx="74" cy="74" r="66" fill="none" stroke="url(#ring)" stroke-width="14"/>
          <g fill="none" stroke="#222" stroke-width="1.6"><circle cx="60" cy="60" r="4"/><circle cx="88" cy="60" r="4"/><circle cx="74" cy="78" r="4"/><path d="M54 72q6-6 12 0M82 72q6-6 12 0M68 90q6-6 12 0"/><path d="M64 82l-4 4M84 82l4 4" stroke-dasharray="2 2"/></g></svg>
        <p>Safety risks, social distancing issues</p>
      </div>
      <div class="problem-item" style="left:602px">
        <svg width="148" height="148" viewBox="0 0 148 148"><circle cx="74" cy="74" r="66" fill="none" stroke="url(#ring)" stroke-width="14"/>
          <g fill="none" stroke="#222" stroke-width="1.6"><circle cx="74" cy="62" r="8"/><path d="M60 92v-8q0-8 8-9h12q8 1 8 9v8z"/><path d="M74 75v10"/></g></svg>
        <p>Legal liabilities, co-employment issues</p>
      </div>
      <div class="problem-item" style="left:787px">
        <svg width="148" height="148" viewBox="0 0 148 148"><circle cx="74" cy="74" r="66" fill="none" stroke="url(#ring)" stroke-width="14"/>
          <g fill="none" stroke="#222" stroke-width="1.6"><path d="M60 56h28M66 56v-4h16v4"/><rect x="69" y="56" width="10" height="20"/><path d="M74 76v14M70 92h8M64 94h20"/></g></svg>
        <p>Distraction due to plant upsets, or site interferences</p>
      </div>
    </div>
  </section>

  <section class="solution band" role="img" aria-label="Dark photograph of refinery pipework and steel structures">
    <div class="copy">
      <h2 class="heading">General Solution</h2>
      <p>A customizable solution that you pay for one time. That reduces the owner’s risk, is not impacted by site conditions or limitations, is transparent, and accountable for planning and scheduling turnarounds.</p>
      <span class="btn">Discover</span>
    </div>
  </section>

  <section class="intro">
    <div class="mark"><span class="dot"></span><span class="name">LQV</span></div>
    <div class="copy">
      <h2 class="heading">Introduce Product</h2>
      <p>Distant Charting and Rostering is a new way of providing the same process of developing job plans, work packages, and turnaround schedules for a fraction of the cost of conventional methods</p>
    </div>
  </section>

  <section class="how band" role="img" aria-label="Night photograph of an illuminated refinery skyline">
    <h2 class="heading">How It Works</h2>
    <div class="how-col" style="left:247px">
      <h3>GENERA</h3>
      <p>LQV still follows all the industry rules for planning and scheduling. But we now are able to perform a large portion of the processes off-site / remotely. By doing this reduces cost, minimizes client’s exposer to legal liabilities, and can improve efficiencies.</p>
      <span class="btn">Read More</span>
    </div>
    <div class="how-col" style="left:740px">
      <h3>SPECIFIC</h3>
      <p>How LQV works: An onsite team is to collects all the necessary information required to develop job plans. Then share it with the remote team using a planning software that both sides can access. The remote team then uses the information and documents to</p>
      <span class="btn">Read More</span>
    </div>
  </section>

  <section class="value">
    <div class="eyebrow">Exclusive Benefits</div>
    <h2 class="heading">Value Prop</h2>
    <p>Clients no longer have to struggle with the recruiting process and reviewing resumes to find the right candidates. LQV is able to attract top resources, that will consistently deliver a product that you will pay for once. No overtime or perdiem cost, just a simple fixed rate per package is all you will have to pay.&nbsp; We will minimize our client’s exposure to legal liabilities and co-employment issues that do come</p>
    <span class="btn">Read More</span>
  </section>

  <section class="contact band" role="img" aria-label="Dark photograph of industrial piping">
    <h2 class="heading">CONTACT US</h2>
    <p>Give WEN a call and ask about our Distant Charting And Rostering services and how we can provide a solution for your next turnaround that will create savings for you.</p>
    <span class="btn">Read More</span>
  </section>

  <footer class="site-footer">
    <div class="footer-brand">
      <div class="brand-row"><span class="dot"></span><span class="name">LQV</span></div>
      <p>LQV, a member of the WEN family of companies, helps remove STO risk by providing the full solution of technology, processes, and personnel deployed onsite throughout the execution of your STO event or capital project</p>
    </div>
    <div class="footer-col" style="left:425px">
      <h4>QUICK LINKS</h4>
      <ul><li>ABOUT US</li><li>Q4METRIC</li><li>SUPPORT</li><li>CONTACT</li></ul>
    </div>
    <div class="footer-col" style="left:590px">
      <h4>CONTACT US</h4>
      <ul>
        <li><svg width="9" height="9" viewBox="0 0 10 10"><path d="M1 5L5 1l4 4v4H6V6H4v3H1z" fill="#222"/></svg><span>4800 Harbor Road, Ste.<br>310 Pinecrest, Texas 7700</span></li>
        <li><svg width="9" height="9" viewBox="0 0 10 10"><path d="M2 1l2 2-1 1.5q1 2 2.5 2.5L7 6l2 2-1.5 1.5Q2 9 .5 2.5z" fill="#222"/></svg><span>+1 555-014-2290</span></li>
        <li><svg width="9" height="9" viewBox="0 0 10 10"><rect x="0.5" y="2" width="9" height="6" fill="#222"/><path d="M.5 2L5 5.5 9.5 2" stroke="#fff" stroke-width=".8" fill="none"/></svg><span>info@mulvarde-example.com</span></li>
      </ul>
    </div>
    <div class="footer-col" style="left:782px">
      <h4>FOLLOW US</h4>
      <div class="social"><span></span><span></span><span></span><span></span></div>
    </div>
  </footer>
  <div class="copyright">Copyright ©2021 Hearthline All Rights Reserved</div>

</main>
</body>
</html>
```